依頼詳細
①手書きのデータを基に作成
②ロゴは添付のものを使用(※変更しないでください)
③自習室のデータは添付のものを使用(※文章の内容は変更不可、イメージ・配置等は変更可)

※東陽電鉄の「30駅制覇フェア」のようなイメージで作成して頂ければと思いますが、良いものであれば、上記のものと全く異なるものでも構いません。
http://ko-tosora.example/tosora30/
記載項目
依頼詳細をご確認ください。
サイズ
A4とB4の2種類
ページ数
片面
希望イメージ
シンプル 複雑
単色 カラフル
暗い 明るい
日常 高級
遊び心 厳粛
未来的 伝統的
女性的 男性的
希望する色
水色系、緑系、黄・オレンジ系
納品ファイル
• 高解像度JPG (.jpg)
• イラストレーター形式 (.ai)
補足説明
自習室データは別途お送りします。
自習室のデータはこちらでお願いします。
納期を11日に変更させて頂きました。
期限を延長させて頂きます。

```html
<!DOCTYPE html>
<html lang="ja">
<head>
<meta charset="utf-8">
<title>個別指導ひかり 20教室達成キャンペーン</title>
<link rel="stylesheet" href="https://fonts.googleapis.com/css2?family=M+PLUS+Rounded+1c:wght@500;800;900&family=Noto+Sans+JP:wght@400;700;900&family=Shippori+Mincho:wght@700&display=swap">
<style>
:root{
  --sky:#5fc3ee;
  --blue:#1565b8;
  --navy:#0d3f86;
  --green:#3aa54a;
  --yellow:#ffe14a;
  --gold:#f2b705;
  --gold-edge:#c98a00;
  --red:#e3262d;
  --blossom:#f6a6c8;
  --white:#fff;
  --ink:#222;
}
*{margin:0;padding:0;box-sizing:border-box}
html,body{width:850px;height:1200px;overflow:hidden}
body{font-family:"Noto Sans JP",sans-serif;color:var(--ink);background:var(--white)}
.flyer{position:relative;width:850px;height:1200px;overflow:hidden;
  background:radial-gradient(circle at 50% 40%,#e4f6fd 0,#9fdcf6 45%,var(--sky) 100%)}
.header{position:absolute;left:0;top:0;width:850px;height:96px;background:var(--white);
  display:flex;align-items:center;justify-content:space-between;padding:0 20px}
.brand{display:flex;align-items:center;gap:10px;white-space:nowrap}
.brand-mark{width:58px;height:58px;background:var(--green);border-radius:6px;flex:none}
.brand-name{font-family:"M PLUS Rounded 1c",sans-serif;font-weight:900;color:var(--blue);font-size:46px;line-height:1}
.header-tagline{background:var(--blue);color:var(--white);border-radius:6px;padding:6px 12px;width:360px;
  font-weight:700;font-size:14px;line-height:1.4;white-space:nowrap}
.header-tagline .pill{display:inline-block;background:var(--white);color:var(--red);border-radius:3px;padding:0 4px;margin-right:4px}
.header-tagline .grades{display:block;text-align:center;background:var(--yellow);color:var(--navy);border-radius:3px;margin-top:3px;font-weight:900}
.region{position:absolute;top:106px;width:100%;text-align:center;color:var(--white);
  font-family:"M PLUS Rounded 1c",sans-serif;font-weight:900;font-size:40px;letter-spacing:3px;white-space:nowrap;
  text-shadow:0 0 6px var(--blue),0 0 2px var(--blue)}
.card{position:absolute;left:42px;top:170px;width:766px;height:460px;background:rgba(255,255,255,.93);
  border-radius:22px;border:4px solid var(--white)}
.celebrate{position:absolute;left:0;top:0;width:100%;height:200px;white-space:nowrap}
.celebrate .lead{position:absolute;left:390px;top:8px;font-family:"Shippori Mincho",serif;font-size:26px;line-height:1.2;color:var(--navy)}
.celebrate .lead2{position:absolute;left:420px;top:42px;font-family:"Shippori Mincho",serif;font-size:26px;line-height:1.2;color:var(--navy)}
.celebrate .iwai{position:absolute;left:120px;top:64px;width:100px;height:100px;border-radius:50%;background:var(--blossom);
  color:var(--white);font-family:"Shippori Mincho",serif;font-size:54px;display:flex;align-items:center;justify-content:center}
.celebrate .count{position:absolute;left:236px;top:22px;font-family:"M PLUS Rounded 1c",sans-serif;font-weight:900;
  font-size:132px;line-height:1;color:var(--gold);-webkit-text-stroke:3px var(--gold-edge)}
.celebrate .achieve{position:absolute;left:420px;top:82px;font-family:"M PLUS Rounded 1c",sans-serif;font-weight:900;
  font-size:62px;line-height:1;color:var(--gold);-webkit-text-stroke:2px var(--gold-edge)}
.celebrate .campaign{position:absolute;left:236px;top:152px;font-family:"M PLUS Rounded 1c",sans-serif;font-weight:900;
  font-size:38px;line-height:1;color:var(--gold);-webkit-text-stroke:1px var(--gold-edge);letter-spacing:4px}
.perks{position:absolute;left:18px;top:204px;width:722px;display:flex;justify-content:space-between}
.perk{width:228px;height:150px;border-radius:50%;background:var(--yellow);text-align:center;padding-top:8px;
  font-weight:900;color:var(--navy);font-size:17px;line-height:1.3;white-space:nowrap}
.perk .num{display:block;font-family:"M PLUS Rounded 1c",sans-serif;font-size:34px;color:var(--red);font-style:italic;line-height:1.05}
.perk em{font-style:normal;color:var(--red);font-size:21px}
.perk .hl{background:var(--red);color:var(--white);padding:0 4px}
.note{position:absolute;left:0;top:358px;width:100%;text-align:center;font-size:11px;color:#555}
.free{position:absolute;left:22px;top:374px;width:722px;display:flex;align-items:center;justify-content:center;gap:8px;
  font-family:"M PLUS Rounded 1c",sans-serif;font-weight:900;color:var(--blue);white-space:nowrap}
.free .tag{background:var(--red);color:var(--white);font-size:28px;padding:2px 8px;border-radius:4px}
.free .months{font-size:52px;line-height:1}
.free .times{background:var(--red);color:var(--white);font-size:16px;width:38px;line-height:1.1;text-align:center;padding:3px 0;border-radius:4px}
.free .fee{font-size:52px;line-height:1}
.free .zero{font-size:80px;color:var(--red);line-height:.9}
.free .yen{font-size:34px;color:var(--red);align-self:flex-end}
.more{position:absolute;top:630px;left:0;width:100%;text-align:center;font-weight:900;color:var(--white);font-size:20px;
  text-shadow:0 0 4px var(--blue)}
.deal{position:absolute;left:42px;width:766px;height:56px;display:flex;align-items:center;white-space:nowrap;
  background:var(--white);border:3px solid var(--sky);border-radius:28px;padding:0 18px;gap:8px}
.deal-pair{top:662px}
.deal-trio{top:728px}
.deal .cond{flex:1;font-weight:700;font-size:16px;line-height:1.25;color:var(--ink)}
.deal .plus{font-family:"M PLUS Rounded 1c",sans-serif;font-weight:900;font-size:36px;color:var(--sky)}
.deal .term{font-family:"M PLUS Rounded 1c",sans-serif;font-weight:900;font-size:30px;color:var(--blue)}
.deal .half{background:var(--red);color:var(--white);font-weight:900;font-size:28px;padding:0 10px;border-radius:4px}
.study{position:absolute;left:20px;top:796px;width:810px;height:392px;background:var(--white);border-radius:14px;border:3px solid var(--green)}
.study .badge{position:absolute;left:10px;top:10px;width:110px;height:66px;background:var(--green);color:var(--white);
  font-weight:900;font-size:16px;line-height:1.25;text-align:center;padding-top:10px;border-radius:8px;white-space:nowrap}
.study .title{position:absolute;left:130px;top:16px;height:50px;padding:0 14px;border:3px solid var(--gold);border-radius:25px;
  background:var(--yellow);display:flex;align-items:center;gap:8px;white-space:nowrap;
  font-family:"M PLUS Rounded 1c",sans-serif;font-weight:900;color:var(--navy);font-size:22px}
.study .title small{font-size:12px;background:var(--green);color:var(--white);padding:2px 6px;border-radius:4px}
.study .body{position:absolute;left:18px;top:96px;width:540px;font-size:13px;line-height:1.8}
.study .photo{position:absolute;border-radius:8px}
.photo-a{left:586px;top:14px;width:206px;height:174px;background:linear-gradient(135deg,#d8d2c4,#a9b6c2)}
.photo-b{left:586px;top:198px;width:206px;height:174px;background:linear-gradient(135deg,#cfd9cf,#9aa8b0)}
</style>
</head>
<body>
<main class="flyer">
  <header class="header">
    <div class="brand">
      <span class="brand-mark"></span>
      <span class="brand-name">個別指導ひかり</span>
    </div>
    <p class="header-tagline">圧倒的指導力と面倒見に自信があるから<br>
      <span class="pill">中学受験</span><span class="pill">私立中学生</span>にもしっかり対応!
      <span class="grades">小・中・高・全学年指導</span></p>
  </header>

  <h1 class="region">泉州地域No.1の塾へ</h1>

  <section class="card">
    <div class="celebrate">
      <p class="lead">多くの皆様に</p>
      <p class="lead2">支持されて</p>
      <span class="iwai">祝</span>
      <span class="count">20</span>
      <span class="achieve">教室達成!</span>
      <span class="campaign">キャンペーン</span>
    </div>

    <div class="perks">
      <p class="perk"><span class="num">1</span>2回の<br>体験授業を<br><span class="hl">無料</span>で受講</p>
      <p class="perk"><span class="num">2</span>体験後に入塾で<br><em>6回分</em>授業を<br>プレゼント!</p>
      <p class="perk"><span class="num">3</span>入会金<br>(16,200円)も<br>今なら<em>0円!</em></p>
    </div>
    <p class="note">※当校規定の条件を満たした場合に限ります</p>

    <div class="free">
      <span class="tag">最大</span>
      <span class="months">2ヶ月間</span>
      <span class="times">8<br>回分</span>
      <span class="fee">授業料</span>
      <span class="zero">0</span><span class="yen">円</span>
    </div>
  </section>

  <p class="more">さらに</p>
  <div class="deal deal-pair">
    <p class="cond">お友達・兄弟姉妹、2人同時に<br>ご入塾の場合は</p>
    <span class="plus">+</span><span class="term">1ヶ月間</span><span class="term">授業料</span><span class="half">半額!</span>
  </div>
  <div class="deal deal-trio">
    <p class="cond">3人同時にご入塾の場合は</p>
    <span class="plus">+</span><span class="term">2ヶ月間</span><span class="term">授業料</span><span class="half">半額!</span>
  </div>

  <section class="study">
    <p class="badge">自習室<br>ここが違う!</p>
    <h2 class="title">いつでも使える自習室! <small>土曜日・日曜日も解放!</small></h2>
    <p class="body">授業のない日も自由に使える自習室を用意しています。わからない問題は講師にすぐ質問できるので、家では集中できない人も安心です。定期テスト前や受験期には長時間の学習にも対応し、静かな環境で一人ひとりの目標達成をしっかり支えます。</p>
    <div class="photo photo-a" role="img" aria-label="自習室で生徒が勉強している写真"></div>
    <div class="photo photo-b" role="img" aria-label="明るい自習室の机が並ぶ教室の写真"></div>
  </section>
</main>
</body>
</html>
```